Corvella Santoro Winery 2023 Label

We are just about to bottle our very first Napa Valley Cabernet Sauvignon and need label ideas

Target Market(s)

Cab drinkers who like Napa California Cabs

Industry/Entity Type

Wine Making

Logo Text

Corvella Santoro 2023 Napa Estate Grown Cabernet Sauvignon

Requirements
Must have
• Winery Name, year of vintage and Napa Estate Cab
Nice to have
• If using the initials C and S use gold letters on black or red background

```html
<!DOCTYPE html>
<html lang="en">
<head>
<meta charset="utf-8">
<title>Corvella Santoro Winery – Napa Valley Cabernet Sauvignon 2023 Label</title>
<link rel="stylesheet" href="https://fonts.googleapis.com/css2?family=Playfair+Display:ital,wght@0,700;0,900;1,700;1,900&family=Montserrat:wght@400&family=Great+Vibes&display=swap">
<style>
  :root {
    --backdrop: #a29c9a;
    --paper: #ede8e1;
    --paper-edge: #e2dbd1;
    --wine: #6e1420;
    --ink: #141111;
    --sketch-light: #c9d0d4;
    --sketch-dark: #8f9ba2;
    --grey-text: #6b6766;
  }
  * { margin: 0; padding: 0; box-sizing: border-box; }
  html, body { width: 1200px; height: 1200px; overflow: hidden; }
  body {
    background: var(--backdrop);
    display: flex;
    align-items: center;
    justify-content: center;
  }
  .label {
    position: relative;
    width: 820px;
    height: 1000px;
    background: radial-gradient(ellipse at 50% 40%, var(--paper) 60%, var(--paper-edge) 100%);
    box-shadow: 0 18px 50px rgba(0,0,0,0.25);
  }
  .estate-illustration {
    position: absolute;
    left: 60px;
    top: 70px;
    width: 700px;
    height: 360px;
    background: radial-gradient(ellipse at 50% 60%, var(--sketch-dark) 0%, var(--sketch-light) 55%, rgba(237,232,225,0) 78%);
  }
  .varietal-title {
    position: absolute;
    top: 470px;
    width: 100%;
    text-align: center;
    font-family: "Playfair Display", serif;
    font-style: italic;
    font-weight: 900;
    color: var(--wine);
    font-size: 62px;
    line-height: 1.12;
    letter-spacing: 4px;
  }
  .brand-name {
    position: absolute;
    top: 650px;
    width: 100%;
    text-align: center;
    font-family: "Playfair Display", serif;
    font-weight: 700;
    font-size: 30px;
    color: var(--wine);
    letter-spacing: 1px;
  }
  .cantina-row {
    position: absolute;
    top: 748px;
    left: 0;
    width: 100%;
    display: flex;
    align-items: center;
    justify-content: center;
    gap: 26px;
  }
  .rule {
    display: block;
    width: 110px;
    height: 2px;
    background: var(--wine);
  }
  .cantina {
    font-family: "Montserrat", sans-serif;
    font-weight: 400;
    font-size: 24px;
    letter-spacing: 9px;
    color: var(--grey-text);
  }
  .winery-name {
    position: absolute;
    top: 782px;
    width: 100%;
    text-align: center;
    font-family: "Playfair Display", serif;
    font-weight: 900;
    font-size: 34px;
    color: var(--ink);
  }
  .winery-name .script {
    font-family: "Great Vibes", cursive;
    font-weight: 400;
    font-size: 38px;
    color: var(--wine);
    margin: 0 8px;
  }
  .vintage-row {
    position: absolute;
    top: 840px;
    width: 100%;
    display: flex;
    align-items: center;
    justify-content: center;
    gap: 70px;
  }
  .vintage-row .rule { width: 50px; }
  .vintage {
    font-family: "Playfair Display", serif;
    font-weight: 900;
    font-size: 32px;
    color: var(--ink);
  }
  .legal {
    position: absolute;
    bottom: 60px;
    font-family: "Playfair Display", serif;
    font-weight: 700;
    font-size: 20px;
    color: var(--ink);
  }
  .legal-volume { left: 50px; }
  .legal-abv { right: 110px; }
</style>
</head>
<body>
  <main class="label">
    <div class="estate-illustration" role="img" aria-label="Grey-blue pencil sketch of a hilltop farmhouse with cypress trees above rows of vineyard"></div>

    <h1 class="varietal-title">Napa Valley<br>Cabernet Sauvignon</h1>

    <p class="brand-name">Corvella Santoro</p>

    <div class="cantina-row">
      <span class="rule"></span>
      <span class="cantina">CANTINA</span>
      <span class="rule"></span>
    </div>

    <p class="winery-name">Corvella<span class="script">Santoro</span>Winery</p>

    <div class="vintage-row">
      <span class="rule"></span>
      <span class="vintage">2023</span>
      <span class="rule"></span>
    </div>

    <p class="legal legal-volume">750 ml ℮</p>
    <p class="legal legal-abv">13% vol</p>
  </main>
</body>
</html>
```